New ante natal classes need competitive poster design

I am starting a new independent childbirth preparation business. There is a lot of competition from "trendy" practitioners locally. As an older and experienced childbirth educator I need to have a different appeal and image - That of experience/wisdom/grandmotherliness whilst being up to date with latest thinking . I am a mother of four and grandmother and have prepared over 1000 women for birth. The design needs to give a modern take on tradition with a mother and baby context. The name of my business is "tidal cradle", the poster will need to be sufficiently different to stand out on any notice board. Text as follows:
tidal cradle
Birth and parenthood classes using the most effective preparation techniques run by experienced BPA teacher/trainer
Classes cover:
choices in childbirth
normal pregnancy, labour and variations
self help techniques for labour including hypno-birthing
breastfeeding
baby care and paediatric first aid

Call 07448213097

```html
<!DOCTYPE html>
<html lang="en">
<head>
<meta charset="utf-8">
<title>tidal cradle – birth and parenthood classes</title>
<link rel="stylesheet" href="https://fonts.googleapis.com/css2?family=Nunito:wght@900&family=Baloo+2:wght@800&family=PT+Serif:wght@700&display=swap">
<style>
  :root {
    --page: #ffffff;
    --magenta: #ec2f72;
    --band-orange: #f6964e;
    --band-blue: #5fb6eb;
    --band-green: #5ec29c;
    --band-lavender: #b9acd1;
    --band-pink: #f7628f;
    --title-fill: #ffffff;
    --title-edge: #2b1670;
    --strap: #f8f032;
    --item-ink: #2a1f33;
    --light: #ffffff;
  }
  html, body {
    margin: 0;
    padding: 0;
    width: 838px;
    height: 1200px;
    overflow: hidden;
    background: var(--page);
  }
  .poster {
    display: block;
    width: 838px;
    height: 1200px;
  }
  .sheet { fill: var(--magenta); }
  .band-orange { fill: var(--band-orange); }
  .band-blue { fill: var(--band-blue); }
  .band-green { fill: var(--band-green); }
  .band-lavender { fill: var(--band-lavender); }
  .band-pink { fill: var(--band-pink); }
  .brand-name {
    font-family: "Nunito", sans-serif;
    font-weight: 900;
    font-size: 86px;
    fill: var(--title-fill);
    stroke: var(--title-edge);
    stroke-width: 5px;
    paint-order: stroke;
    stroke-linejoin: round;
  }
  .strapline {
    font-family: "Baloo 2", sans-serif;
    font-weight: 800;
    font-size: 22px;
    fill: var(--strap);
  }
  .cover-heading {
    font-family: "Baloo 2", sans-serif;
    font-weight: 800;
    font-size: 30px;
    fill: var(--light);
  }
  .class-topic {
    font-family: "Baloo 2", sans-serif;
    font-weight: 800;
    font-size: 19px;
    fill: var(--item-ink);
  }
  .call-label, .call-number {
    font-family: "PT Serif", serif;
    font-weight: 700;
    fill: var(--light);
  }
  .call-label { font-size: 32px; }
  .call-number { font-size: 31px; }
</style>
</head>
<body>
<svg class="poster" viewBox="0 0 620 888" preserveAspectRatio="none" xmlns="http://www.w3.org/2000/svg">
  <defs>
    <clipPath id="sheet-clip">
      <rect x="10" y="15" width="600" height="860"/>
    </clipPath>
    <linearGradient id="placeholder-tone" x1="0" y1="0" x2="0" y2="1">
      <stop offset="0" stop-color="#ffffff" stop-opacity="0.6"/>
      <stop offset="0.5" stop-color="#ffffff" stop-opacity="0.4"/>
      <stop offset="1" stop-color="#ffffff" stop-opacity="0.15"/>
    </linearGradient>
  </defs>

  <rect class="sheet" x="10" y="15" width="600" height="860"/>

  <g class="rainbow" clip-path="url(#sheet-clip)">
    <path class="band-orange" d="M10 228 Q310 374 610 440 L610 500 Q310 437 10 293 Z"/>
    <path class="band-blue" d="M10 293 Q310 437 610 500 L610 590 Q310 516 10 362 Z"/>
    <path class="band-green" d="M10 362 Q310 516 610 590 L610 690 Q310 605 10 440 Z"/>
    <path class="band-lavender" d="M10 440 Q310 605 610 690 L610 790 Q310 697 10 525 Z"/>
    <path class="band-pink" d="M10 525 Q310 697 610 790 L610 875 Q330 900 10 700 Z"/>
  </g>

  <rect class="figure-placeholder" x="330" y="330" width="280" height="545" rx="40" fill="url(#placeholder-tone)" clip-path="url(#sheet-clip)" role="img" aria-label="Translucent silhouette of a mother seated holding her baby"/>

  <text class="brand-name" x="313" y="110" text-anchor="middle" textLength="474" lengthAdjust="spacingAndGlyphs">tidal cradle</text>

  <g class="strap">
    <text class="strapline" x="314" y="170" text-anchor="middle" textLength="472" lengthAdjust="spacingAndGlyphs">Birth and parenthood classes using the most</text>
    <text class="strapline" x="314" y="201" text-anchor="middle" textLength="418" lengthAdjust="spacingAndGlyphs">effective preparation techniques run by</text>
    <text class="strapline" x="314" y="231" text-anchor="middle" textLength="338" lengthAdjust="spacingAndGlyphs">experienced BPA teacher/trainer</text>
  </g>

  <text class="cover-heading" transform="translate(168 320) rotate(23)" textLength="225" lengthAdjust="spacingAndGlyphs">Classes cover:</text>

  <g class="topics">
    <text class="class-topic" transform="translate(100 342) rotate(28)" textLength="188" lengthAdjust="spacingAndGlyphs">choices in childbirth</text>
    <text class="class-topic" transform="translate(100 436) rotate(22.5)" textLength="362" lengthAdjust="spacingAndGlyphs">normal pregnancy, labour and variations</text>
    <text class="class-topic" transform="translate(95 511) rotate(19)" textLength="500" lengthAdjust="spacingAndGlyphs">self help techniques for labour including hypno-birthing</text>
    <text class="class-topic" transform="translate(174 636) rotate(30)" textLength="128" lengthAdjust="spacingAndGlyphs">breastfeeding</text>
    <text class="class-topic" transform="translate(50 640) rotate(34.5)" textLength="306" lengthAdjust="spacingAndGlyphs">baby care and paediatric first aid</text>
  </g>

  <g class="contact">
    <text class="call-label" x="121" y="827" text-anchor="middle">Call</text>
    <text class="call-number" x="30" y="866" textLength="180" lengthAdjust="spacingAndGlyphs">07448213097</text>
  </g>
</svg>
</body>
</html>
```